Postcard Design for Marketing to Builders

I am an architect that gets most of my work from contractor's. I design residential and commercial projects based in California. My main focus is California's Central Coast. I want the feel of the postcard to reflect a strong professional, efficient and creative partner for contractors (Builders). I have provide some photos of projects I have done recently to use on the postcard if needed. I have also included my logo which I would like on the front.

Industry/Entity Type

Architect

Font styles to use
Serif

```html
<!DOCTYPE html>
<html lang="en">
<head>
<meta charset="utf-8">
<title>Daniel R Hale Architect – Postcard</title>
<link rel="stylesheet" href="https://fonts.googleapis.com/css2?family=Source+Sans+3:wght@400;600&display=swap">
<style>
:root{
  --navy:#2f3a9c;
  --navy-dark:#27318a;
  --orange:#ef6a1f;
  --ink:#1c1c1c;
  --grey-text:#6b6b6b;
  --beige:#e2ddce;
  --line:#b9b9b9;
  --paper:#ffffff;
  --bg:#ecebe8;
}
*{box-sizing:border-box;margin:0;padding:0}
html,body{width:1128px;height:1200px;overflow:hidden;background:var(--bg)}
body{position:relative;font-family:"Source Sans 3",Arial,sans-serif;color:var(--ink)}

.card{position:absolute;background:var(--paper);box-shadow:0 6px 18px rgba(0,0,0,.25);overflow:hidden}
.card--front{left:103px;top:15px;width:862px;height:561px}
.card--back{left:167px;top:611px;width:860px;height:558px}

/* front */
.front-art{position:absolute;inset:0}
.brand{position:absolute;text-align:center}
.card--front .brand{left:60px;top:118px;width:320px}
.brand__name{display:flex;align-items:center;justify-content:center;gap:10px;
  font-weight:600;color:var(--navy);font-size:31px;letter-spacing:.5px;text-transform:uppercase;line-height:1}
.brand__mark{width:16px;height:16px;background:var(--orange)}
.brand__tag{margin-top:6px;font-size:13px;font-weight:600;letter-spacing:8px;color:var(--orange)}
.front-copy{position:absolute;left:42px;top:240px;font-size:18px;line-height:24px}
.front-copy .lead{margin-bottom:8px}
.phone{display:flex;align-items:center;gap:10px;margin-top:12px;font-size:20px}
.phone svg{flex:none}
.thumb{position:absolute;top:388px;width:203px;height:123px;border:2px solid #fff;box-shadow:0 1px 4px rgba(0,0,0,.2)}
.thumb--1{left:42px;background:linear-gradient(180deg,#cfe1f0 0%,#d8b9a0 45%,#9b9182 100%)}
.thumb--2{left:266px;background:linear-gradient(180deg,#a9c48a 0%,#6d7a74 45%,#5f8f3e 100%)}
.thumb--3{left:489px;background:linear-gradient(180deg,#e6e9ec 0%,#a64a2a 45%,#5c4a3e 100%)}

/* back */
.back-logo{position:absolute;left:0;top:0;width:315px;height:195px;background:#fff}
.card--back .brand{left:10px;top:80px;width:295px}
.card--back .brand__name{font-size:27px}
.card--back .brand__tag{font-size:12px;letter-spacing:7px}
.back-photo{position:absolute;left:315px;top:0;width:165px;height:195px;
  background:linear-gradient(180deg,#bcd6ef 0%,#d9d2c2 30%,#6f7a80 60%,#7aa048 85%,#e5cf3a 100%)}
.specialities{position:absolute;left:0;top:195px;width:480px;height:238px;background:var(--beige);
  padding:14px 17px 0 34px;color:var(--grey-text);font-size:16px;line-height:21px}
.specialities h2{font-size:16px;font-weight:400;margin-bottom:20px}
.specialities p{text-align:justify;hyphens:auto;-webkit-hyphens:auto}
.cta{position:absolute;left:0;top:444px;width:480px;height:89px;
  background:linear-gradient(90deg,var(--navy-dark),#3d4bb3);color:#fff;text-align:center;padding-top:10px}
.cta__line{font-size:23px}
.cta__phone{display:flex;align-items:center;justify-content:center;gap:12px;font-size:27px;margin-top:4px}
.sender{position:absolute;left:500px;top:31px;color:var(--ink)}
.sender__name{font-size:20px;color:var(--navy-dark)}
.sender__role{font-size:14px;margin-bottom:10px}
.sender__info{font-size:11.5px;line-height:15px;color:#333}
.stamp{position:absolute;left:730px;top:24px;width:104px;height:87px;border:1.5px solid var(--line)}
.address-lines{position:absolute;left:505px;top:205px;width:329px}
.address-lines span{display:block;height:1.5px;background:var(--line);margin-bottom:41.5px}
</style>
</head>
<body>

<section class="card card--front" aria-label="Postcard front">
  <svg class="front-art" width="862" height="561" viewBox="0 0 862 561">
    <defs>
      <linearGradient id="faint" x1="0" y1="0" x2="0" y2="1">
        <stop offset="0" stop-color="#f7f6f3"/><stop offset="1" stop-color="#ecebe6"/>
      </linearGradient>
      <linearGradient id="building" x1="0" y1="0" x2="0" y2="1">
        <stop offset="0" stop-color="#7fa6d6"/>
        <stop offset=".3" stop-color="#c9b08a"/>
        <stop offset=".65" stop-color="#b59a72"/>
        <stop offset="1" stop-color="#6f7a4e"/>
      </linearGradient>
    </defs>
    <rect width="862" height="561" fill="url(#faint)" role="img" aria-label="Faded photo of a commercial building behind the text"/>
    <polygon points="355,0 862,0 862,561 720,561 415,247" fill="url(#building)" role="img" aria-label="Photo of a completed three-storey commercial building"/>
    <polygon points="640,0 662,0 505,160 490,150" fill="#ffffff" opacity=".85"/>
    <polygon points="662,0 700,0 560,140 540,128" fill="#ffffff" opacity=".25"/>
  </svg>

  <div class="brand">
    <div class="brand__name"><span class="brand__mark"></span>Daniel R Hale</div>
    <div class="brand__tag">ARCHITECT</div>
  </div>

  <div class="front-copy">
    <p class="lead">Licensed architect for almost 25 years</p>
    <p>DESIGN RESIDENTIAL AND COMMERCIAL<br>PROJECTS BASED IN CALIFORNIA</p>
    <p class="phone">
      <svg width="22" height="22" viewBox="0 0 24 24" aria-hidden="true"><circle cx="12" cy="12" r="10.5" fill="none" stroke="#1c1c1c" stroke-width="1.8"/><path d="M8.2 6.5l2 2.3-1.2 1.5c.8 1.7 2 2.9 3.7 3.7l1.5-1.2 2.3 2-1.2 1.8c-3.8-.3-7.6-4.1-7.9-7.9z" fill="#1c1c1c"/></svg>
      (805) 555-0142
    </p>
  </div>

  <div class="thumb thumb--1" role="img" aria-label="Photo of a two-storey stucco home with garage"></div>
  <div class="thumb thumb--2" role="img" aria-label="Photo of a craftsman house with a front porch among trees"></div>
  <div class="thumb thumb--3" role="img" aria-label="Photo of a timber-framed entrance canopy"></div>
</section>

<section class="card card--back" aria-label="Postcard back">
  <div class="back-logo">
    <div class="brand">
      <div class="brand__name"><span class="brand__mark"></span>Daniel R Hale</div>
      <div class="brand__tag">ARCHITECT</div>
    </div>
  </div>
  <div class="back-photo" role="img" aria-label="Photo of a glass-walled patio entrance with yellow flowers"></div>

  <div class="specialities">
    <h2>SPECIALITIES:</h2>
    <p>Custom Home Designer, Residential Home Designer, Commercial Office Building, Commercial Tenant Improvements, Retail Tenant Improvement, Residential &amp; Commercial Problem Solver, Architectural Custom Plans, Residential Remodel Design, Client Educational Programs; Builder's Plan Review Clinic, Video Series: Plan It * Draw It * Raise It Your Home Planning Field Notes</p>
  </div>

  <div class="cta">
    <p class="cta__line">Call today for your FREE estimate!</p>
    <p class="cta__phone">
      <svg width="30" height="30" viewBox="0 0 24 24" aria-hidden="true"><circle cx="12" cy="12" r="10.5" fill="none" stroke="#fff" stroke-width="1.6"/><path d="M8.2 6.5l2 2.3-1.2 1.5c.8 1.7 2 2.9 3.7 3.7l1.5-1.2 2.3 2-1.2 1.8c-3.8-.3-7.6-4.1-7.9-7.9z" fill="#fff"/></svg>
      (805) 555-0142
    </p>
  </div>

  <div class="sender">
    <p class="sender__name">Daniel R Hale</p>
    <p class="sender__role">ARCHITECT</p>
    <p class="sender__info">(805) 555-0142<br>PO Box 418, Arroyo Vista,<br>CA 93400</p>
  </div>
  <div class="stamp" aria-label="Stamp area"></div>
  <div class="address-lines" aria-label="Address lines"><span></span><span></span><span></span><span></span><span></span></div>
</section>

</body>
</html>
```